Book Cover Design Project - SIMPLE ART, Pre-Concepted

We already have a full design concept for the cover art. It is however in a low quality word document format. This project is to recreate existing example guideline art in as much vector art possible for great quality print production. Artistic flare is welcome. This will be for a book cover (front/back) and I want the quality to be excellent.

Art to be provided in Adobe Illustrator format. The book will be 6wide x 9high, so the artboard for the cover needs to be set up to 12.5 wide x 9 high with .125" bleeds.

Copy content for the spine: "Beneath the Orchard Lamps at Dusk" RL Ombrisko.

Here is a link to download the word document "template" and a new photo for the back page. I'm not sure that I like the new photo, it is possible the old one in the word document will work.

www.kelmarpressworks.com/uploads/BriefingFilesSetAll.zip

I've got a fast deadline on this project because the client would like to have manufacturing completed by Christmas...which is why this is only a 2 day project. I appreciate your interest in our project.

Gordon

Try this link...seems I was missing the .zip extension which may have been causing problems.

Requirements
Must have
• Adobe Illustrator Files
CMYK color setup - no color definitions for project
Artboard Size: 12.625 wide x 9.125 high
Art Orientation: Flat image should have the back book page on the left side, front page on the right side, spine copy running down the middle.

```html
<!DOCTYPE html>
<html lang="en">
<head>
<meta charset="utf-8">
<title>Beneath the Orchard Lamps at Dusk — Cover Spread</title>
<link rel="stylesheet" href="https://fonts.googleapis.com/css2?family=Cormorant+Garamond:ital,wght@1,600;1,700&family=Open+Sans:wght@400;700&display=swap">
<style>
  :root {
    --page: #ffffff;
    --panel-light: #858585;
    --panel-mid: #5e5e5e;
    --panel-dark: #3d3d3d;
    --ink: #1e1e1e;
    --crimson: #c8102e;
    --lavender: #dcdcef;
    --cross-grey: #8e8e8e;
    --mark: #111111;
  }
  * { margin: 0; padding: 0; box-sizing: border-box; }
  html, body { width: 1200px; height: 1000px; overflow: hidden; background: var(--page); }
  .spread { position: relative; width: 1200px; height: 1000px; }

  .printer-marks { position: absolute; inset: 0; }

  .cover-panel {
    position: absolute; left: 28px; top: 84px; width: 1142px; height: 831px;
    background:
      radial-gradient(ellipse 60% 55% at 22% 20%, rgba(170,170,170,.35), transparent 70%),
      radial-gradient(ellipse 70% 50% at 80% 75%, rgba(120,120,120,.25), transparent 70%),
      linear-gradient(180deg, var(--panel-light) 0%, var(--panel-mid) 45%, var(--panel-dark) 100%);
  }

  /* Back cover */
  .about {
    position: absolute; left: 80px; top: 146px; width: 460px;
    font-family: "Open Sans", sans-serif; font-size: 12.6px; line-height: 15.9px;
    color: var(--ink); text-align: justify; hyphens: auto;
  }
  .about p { margin: 0; }
  .about strong { font-weight: 700; }
  .author-photo {
    float: left; width: 208px; height: 239px; margin: 1px 28px 0 0;
    background: linear-gradient(160deg, #efe2cf 0%, #d9c3a6 45%, #2b2f3a 60%, #1c1f28 100%);
  }

  /* Spine */
  .spine-copy {
    position: absolute; left: 598px; top: 498px;
    transform: translate(-50%, -50%) rotate(90deg);
    white-space: nowrap;
    font-family: "Cormorant Garamond", serif; font-style: italic; font-weight: 700;
    font-size: 17px; color: var(--crimson); letter-spacing: .2px;
  }
  .spine-copy .spine-author { margin-left: 26px; }

  /* Front cover */
  .front-title {
    position: absolute; font-family: "Cormorant Garamond", serif;
    font-style: italic; font-weight: 700; color: var(--crimson);
    font-size: 38px; line-height: 1; white-space: nowrap;
  }
  .title-top { left: 890px; top: 198px; transform: translateX(-50%); letter-spacing: 4px; }
  .title-left { right: 424px; top: 390px; }
  .title-right { left: 1006px; top: 390px; }
  .title-bottom { left: 890px; top: 602px; transform: translateX(-50%); }

  .cross-frame {
    position: absolute; left: 786px; top: 260px; width: 204px; height: 322px;
    border: 1px solid var(--crimson);
    background:
      radial-gradient(ellipse 40% 55% at 50% 50%, rgba(142,142,142,.55), transparent 75%),
      var(--lavender);
  }

  .compilation-line {
    position: absolute; left: 848px; top: 782px; transform: translateX(-50%);
    font-family: "Cormorant Garamond", serif; font-style: italic; font-weight: 700;
    font-size: 21px; color: var(--crimson); white-space: nowrap;
  }
</style>
</head>
<body>
<main class="spread">
  <svg class="printer-marks" width="1200" height="1000" viewBox="0 0 1200 1000" aria-hidden="true">
    <g stroke="var(--mark)" stroke-width="1" fill="none">
      <!-- trim lines -->
      <line x1="40" y1="54" x2="40" y2="80"/><line x1="0" y1="84" x2="24" y2="84"/>
      <line x1="1158" y1="54" x2="1158" y2="80"/><line x1="1176" y1="84" x2="1200" y2="84"/>
      <line x1="40" y1="920" x2="40" y2="946"/><line x1="0" y1="915" x2="24" y2="915"/>
      <line x1="1158" y1="920" x2="1158" y2="946"/><line x1="1176" y1="915" x2="1200" y2="915"/>
      <!-- registration targets -->
      <g id="target"><circle r="6"/><circle r="3"/><line x1="-9" y1="0" x2="9" y2="0"/><line x1="0" y1="-9" x2="0" y2="9"/></g>
      <use href="#target" x="62" y="70"/><use href="#target" x="15" y="114"/>
      <use href="#target" x="1137" y="70"/><use href="#target" x="1184" y="114"/>
      <use href="#target" x="15" y="882"/><use href="#target" x="62" y="928"/>
      <use href="#target" x="1184" y="882"/><use href="#target" x="1137" y="928"/>
    </g>
    <g fill="var(--mark)">
      <circle cx="14" cy="70" r="10"/><circle cx="1186" cy="928" r="10"/>
    </g>
  </svg>

  <div class="cover-panel"></div>

  <section class="about">
    <div class="author-photo" role="img" aria-label="Portrait photograph of the author in a dark suit and striped tie"></div>
    <p><strong>About the author:</strong> The word of God says that “I know the plans I have for you” (Jeremiah 29:11) and that “before I formed you in the womb I knew you” (Jeremiah 1:15). These verses of scripture depict the life of Rowan L Ombrisko.</p>
    <p>As a little boy Rowan was always told that he was going to be a preacher. The magnitude of this repeated statement and exactly what it entailed was not taken seriously or truly understood, at that time. It was not Rowan’s plan or desire to be a preacher, and he tried to do anything and everything to avoid the talks of him becoming one. Rowan’s path of life, although he believed in God, took him down the road that led him away from God. His struggles with life’s events and being an introvert kept him emotionally troubled, in a state of depression and wanting to commit suicide. Yet, as the Lord was with Jeremiah, even so was the Lord with Rowan. The Lord was to show Rowan just what it meant to have complete trust in Him and to know that He would always provide a way of an escape. Before Rowan came to the point of carrying out his plans to commit suicide, he prayed a simple prayer that God would give him a new family. At that exact moment Rowan’s life began to take a new direction. He began to seek after the Lord; it became his quest to find out what it meant to be a servant of God. Because of his being an introvert, he began to write his emotions on paper in the form of poems. Those poems gave him the strength to come out of depression and began his two year journey to find God.</p>
    <p>Rowan’s relationship with Jesus and salvation journey began at the age of nineteen. The poetry writing started as a therapeutic remedy for his troubled past, but developed into the psalms of Rowan because of God’s grace and mercy that delivered him from despair and hopelessness.</p>
    <p>God’s favor covers Rowan’s life and carries him from day to day. It is written that “without me (Christ) ye can do nothing” (John 15:5). This scripture resonates in Rowan’s heart. For, he truly believes that God is the author and he is just the vessel used of God. His desire is that each poem will be taken personally and become a tool used by everyone to help them on their Christian journey and to let them know that they are never alone in their experience and quest to be closer to the Lord Jesus Christ.</p>
  </section>

  <div class="spine-copy">“Beneath the Orchard Lamps at Dusk”<span class="spine-author">RL Ombrisko</span></div>

  <h1 class="front-title title-top">Beneath the</h1>
  <span class="front-title title-left">Orchard</span>
  <div class="cross-frame" role="img" aria-label="Grey wooden cross on a pale lavender field"></div>
  <span class="front-title title-right">Lamps</span>
  <span class="front-title title-bottom">at Dusk</span>

  <p class="compilation-line">A compilation of poems by RL Ombrisko</p>
</main>
</body>
</html>
```